Australian Trucking Company Requires Professional Looking Stationary

We require a professional looking stationary design that incorporates our newly designed logo.

Our business, called "Vell Haulage Contracting", provides contracting work, transport and logistics to business in Western Australia particularly with links to the mining sector.

We are a small business looking to expand and our new logo and our new stationary will help develop our brand image in our market place.

Target Market(s)

Businesses and Corporation with links to the Mining Sector

Industry/Entity Type

Small Business

Requirements
Must have
• The letterhead must have the following details:
The new logo

Text saying: "Vell Haulage Pty Ltd (ACN 582 306 917) ATF The Vell Discretionary Trust T/AS"
"ABN 71 840 239 568"
Address "P.O Box 817 Ashbury WA, 6912"
Phone: 08 9172 5840
Email: vellhaul@mailnest.com.au

The text on the letterhead should be editable as the details are likely to change in the near future. Provision should be made for a website address all though one isn't available at the moment.

The styling, layout and font text is entirely up to the designer.

```html
<!DOCTYPE html>
<html lang="en">
<head>
<meta charset="utf-8">
<title>Vell Haulage Contracting – Business Cards</title>
<link href="https://fonts.googleapis.com/css2?family=Open+Sans:wght@400;600;700&display=swap" rel="stylesheet">
<style>
  :root {
    --red: #d81e27;
    --red-deep: #8c0f15;
    --grey: #8d8d8f;
    --grey-light: #c9c9cb;
    --ink: #4a4a4c;
    --white: #ffffff;
    --backdrop: #ecebe8;
  }
  * { margin: 0; padding: 0; box-sizing: border-box; }
  html, body {
    width: 1200px; height: 407px; overflow: hidden;
    background: var(--backdrop);
    font-family: "Open Sans", Arial, sans-serif;
  }
  .sheet { position: relative; width: 1200px; height: 407px; }
  .card {
    position: absolute; top: 60px;
    width: 502px; height: 288px;
    background: var(--white);
    overflow: hidden;
    box-shadow: 0 4px 10px rgba(0,0,0,0.25);
  }
  .card--front { left: 58px; }
  .card--back { left: 638px; }
  .card__waves { position: absolute; inset: 0; width: 502px; height: 288px; }

  .brand {
    position: absolute; left: 40px; top: 50px;
    display: flex; align-items: center; gap: 14px;
  }
  .brand__mark {
    width: 16px; height: 16px; border-radius: 50%;
    background: var(--red);
  }
  .brand__name {
    font-weight: 700; font-size: 22px; line-height: 24px;
    color: var(--red); text-transform: uppercase; letter-spacing: 0.5px;
  }
  .abn {
    position: absolute; right: 26px; top: 50px;
    font-size: 11px; color: var(--ink);
  }
  .contact {
    position: absolute; left: 42px; top: 186px;
    font-size: 10.5px; line-height: 17px; color: var(--ink);
    list-style: none;
  }
  .contact__address { margin-bottom: 6px; }
  .holder {
    position: absolute; right: 10px; top: 243px; width: 110px;
    text-align: center; color: var(--white);
  }
  .holder__name { font-weight: 700; font-size: 15px; line-height: 18px; }
  .holder__title { font-size: 12px; line-height: 17px; }

  .emblem {
    position: absolute; left: 40px; top: 70px;
    width: 215px; height: 170px; border-radius: 8px;
    background: radial-gradient(ellipse at center, #bdbdbf 0%, #e4e4e6 65%, rgba(255,255,255,0) 100%);
  }
  .web {
    position: absolute; right: 22px; top: 260px;
    font-weight: 700; font-size: 13px; letter-spacing: 2.4px;
    color: var(--white);
  }
</style>
</head>
<body>
<main class="sheet">

  <section class="card card--front" aria-label="Business card front">
    <svg class="card__waves" viewBox="0 0 502 288" aria-hidden="true">
      <defs>
        <radialGradient id="frontRed" cx="0.7" cy="0.6" r="0.7">
          <stop offset="0" stop-color="#ee2a33"/>
          <stop offset="1" stop-color="#8c0f15"/>
        </radialGradient>
        <radialGradient id="frontRedTop" cx="0.2" cy="0.2" r="0.9">
          <stop offset="0" stop-color="#e02129"/>
          <stop offset="1" stop-color="#8c0f15"/>
        </radialGradient>
      </defs>
      <path d="M0 0 H200 C120 8 50 22 0 52 Z" fill="url(#frontRedTop)"/>
      <path d="M60 30 C120 10 200 4 300 2 C210 10 130 20 60 30 Z" fill="var(--grey-light)"/>
      <path d="M0 52 C40 30 110 16 200 8 C120 20 50 40 0 70 Z" fill="var(--grey-light)"/>
      <path d="M0 225 C80 270 200 285 330 240 C400 215 460 175 502 150 V170 C440 205 370 250 260 272 C150 292 60 270 0 245 Z" fill="var(--grey)"/>
      <path d="M400 200 C440 180 470 160 502 140 V150 C470 168 440 186 400 200 Z" fill="var(--grey)"/>
      <path d="M0 245 C60 275 140 290 250 280 C150 288 60 282 0 265 Z" fill="var(--grey-light)"/>
      <path d="M170 288 C290 275 400 230 502 178 V288 Z" fill="url(#frontRed)"/>
    </svg>

    <div class="brand">
      <span class="brand__mark"></span>
      <span class="brand__name">Vell Haulage<br>Contracting</span>
    </div>
    <p class="abn">ABN 71 840 239 568</p>

    <ul class="contact">
      <li class="contact__address">P.O Box 817 Ashbury WA, 6912</li>
      <li>P:&nbsp; 08 9172 5840</li>
      <li>E:&nbsp; vellhaul@mailnest.com.au</li>
      <li>W: www.vellhaulage.com</li>
    </ul>

    <div class="holder">
      <p class="holder__name">Your Name</p>
      <p class="holder__title">Title</p>
    </div>
  </section>

  <section class="card card--back" aria-label="Business card back">
    <svg class="card__waves" viewBox="0 0 502 288" aria-hidden="true">
      <defs>
        <radialGradient id="backRed" cx="0.7" cy="0.6" r="0.7">
          <stop offset="0" stop-color="#ee2a33"/>
          <stop offset="1" stop-color="#8c0f15"/>
        </radialGradient>
        <radialGradient id="backRedTop" cx="0.2" cy="0.2" r="0.9">
          <stop offset="0" stop-color="#e02129"/>
          <stop offset="1" stop-color="#8c0f15"/>
        </radialGradient>
      </defs>
      <path d="M0 0 H120 C70 10 30 28 0 55 Z" fill="url(#backRedTop)"/>
      <path d="M0 55 C40 22 110 6 220 2 C130 14 60 35 0 75 Z" fill="var(--grey-light)"/>
      <path d="M0 250 C90 285 220 285 340 240 C410 212 460 180 502 160 V176 C450 205 390 248 280 272 C160 294 70 280 0 262 Z" fill="var(--grey)"/>
      <path d="M390 205 C430 185 470 162 502 145 V155 C470 172 430 192 390 205 Z" fill="var(--grey)"/>
      <path d="M180 288 C300 276 410 232 502 186 V288 Z" fill="url(#backRed)"/>
    </svg>

    <div class="emblem" role="img" aria-label="Company emblem area in grey tones"></div>
    <p class="web">www.vellhaulage.com</p>
  </section>

</main>
</body>
</html>
```